Fatigued and Overloaded by COVID Messages? We need original illustrations to show that.

Everywhere you look there are messages about COVID. That is leading many people to feel fatigued and overloaded by the messages.

We surveyed U.S. adults March 20th - 24th, 2020 and measured message fatigue, information overload, perceived repetition, and perceived exaggeration. Here is how participants responded:

When it comes to coronavirus . . .
55% feel exhausted by all the messages.
54% feel overloaded by the amount of information.
51% feel that the messages are repetitive.
47% feel like messages exaggerate how bad it is.

In other words, almost half of U.S. adults show signs of message fatigue, information overload, perceived message repetition, and perceived message exaggeration.

We will continue to survey 400 adults every week for the next 16 weeks. Each time we will measure message fatigue, information overload, perceived repetition, and perceived exaggeration. We expect that it will increase over time.

What are we looking for? We need innovative and original illustrations that attempt to communicate these findings. The illustrations would visualize message fatigue, information overload, perceived message repetition, and perceived message exaggeration.

What sort of visual are we looking for? Our preference is for an original illustration (or set of illustrations). Our preference is for creative and powerful illustrations, but we are also open to the creative and well-executed infographics.

We need these images fast . We will award monetary prizes to the 3 best designs. If we like more than that, then we might purchase more (e.g., in past contests, we have purchased as many as 30 designs).

What we will need:
(1) The illustrations must be original and we will need the photoshop and/or illustrator files for all artwork. (By original, we mean that the illustrations are 100% created by you. Our organization requires that we utilize only original illustrated work. We have had issues with free imagery being pirated and reposted as free. We sidestep that issue by just having everything created.)

(2) The illustration should say, somewhere: "Based on a survey of 400 U.S. adults conducted March 20 - 24th, 2020."

(3) We will have almost 4 months worth of data by the time this is done. In other words, the illustrations might be able to help us present that weekly data.

(4) We have conducted other Artvendo projects. It might be helpful to examine designs we liked in the past. For example, here is another COVID project we just finished:

https://jobs.artvendo-example.com/job/5162048

Target Market(s)

U.S. adults

Requirements
Must have
• Original illustrations. Mobile friendly design. People will view this on their smartphones.
Nice to have
• A design that we can use to communicate the data across time.

```html
<!DOCTYPE html>
<html lang="en">
<head>
<meta charset="utf-8">
<title>Percent of Americans to Feel Fatigue and Overloaded by the COVID Messages</title>
<link rel="stylesheet" href="https://fonts.googleapis.com/css2?family=Oswald:wght@500;600&family=Roboto:ital,wght@0,700;0,900;1,700&family=Montserrat:wght@700&display=swap">
<style>
  :root {
    --canvas: #d4f9a4;
    --forest: #33571b;
    --navy: #283593;
    --header-blue: #2e4b9b;
    --header-blue-dark: #1d2f7a;
    --frame-brown: #4a1e08;
    --signal-red: #e8062b;
    --ring-white: #ffffff;
    --gold: #f5b51f;
    --ink: #111111;
    --stat-navy: #253196;
  }
  * { box-sizing: border-box; margin: 0; padding: 0; }
  html, body { width: 1200px; height: 2304px; overflow: hidden; }
  body {
    position: relative;
    background: var(--canvas);
    font-family: "Oswald", "Roboto", sans-serif;
  }
  .abs { position: absolute; }

  .top-band { left: 0; top: 0; width: 1200px; height: 215px; background: var(--forest); }
  .title-box {
    left: 43px; top: 12px; width: 1113px; height: 231px;
    background: var(--frame-brown); padding: 8px;
  }
  .title-box .inner {
    width: 100%; height: 100%;
    background: radial-gradient(ellipse at center, var(--header-blue) 70%, var(--header-blue-dark) 100%);
    text-align: center; color: #fff;
    font-family: "Roboto", sans-serif; font-weight: 900;
    padding-top: 26px;
  }
  .title-box h1 { font-size: 47px; line-height: 60px; letter-spacing: 2px; font-weight: 900; }
  .title-box .source {
    color: var(--gold); font-style: italic; font-weight: 700;
    font-size: 29px; letter-spacing: 1.5px; margin-top: 4px;
  }

  .band { left: 0; width: 1200px; height: 287px; }
  .band.blue { background: var(--navy); }
  .band.green { background: var(--forest); }
  .tab { height: 58px; padding: 9px 11px 0; }
  .tab.blue { background: var(--navy); }
  .tab.green { background: var(--forest); }
  .tab span {
    display: block; height: 48px; background: #fff; color: var(--ink);
    font-family: "Oswald", sans-serif; font-weight: 500; font-size: 31px;
    line-height: 46px; text-align: center;
  }

  .art { left: 9px; width: 438px; height: 268px; }
  .art.fatigue { background: linear-gradient(180deg, #c5c5c0 0%, #e6f15a 60%, #c0c4c0 72%, #c8c8c8 100%); }
  .art.overload { background: linear-gradient(180deg, #c9c9bd 0%, #ecf54a 62%, #c2c2c2 74%, #cfcfcf 100%); }
  .art.repetition { background: linear-gradient(160deg, #f3f048 0%, #d9ea28 100%); }
  .art.exaggeration { background: linear-gradient(135deg, #f59526 0%, #f8ae3c 100%); }

  .ring { width: 262px; height: 262px; }
  .ring-label {
    width: 262px; text-align: center; color: #fff;
    font-family: "Oswald", sans-serif; font-weight: 500; font-size: 82px; line-height: 1;
  }
  .stat-text {
    left: 746px; color: #fff;
    font-family: "Oswald", sans-serif; font-weight: 500; font-size: 45px; line-height: 47px;
  }

  .bottom-band { left: 3px; top: 1650px; width: 1197px; height: 167px; background: var(--forest); }
  .question-box { left: 46px; top: 1659px; width: 1113px; height: 181px; background: var(--frame-brown); padding: 8px; }
  .question-box .inner {
    width: 100%; height: 100%;
    background: radial-gradient(ellipse at center, var(--header-blue) 70%, var(--header-blue-dark) 100%);
    color: #fff; text-align: center;
    font-family: "Roboto", sans-serif; font-weight: 900; font-size: 47px;
    letter-spacing: 3px; line-height: 66px; padding-top: 22px;
  }

  .summary-ring { left: 44px; top: 1877px; width: 386px; height: 386px; }
  .summary-label {
    left: 44px; top: 2018px; width: 386px; text-align: center;
    color: var(--stat-navy); font-family: "Roboto", sans-serif; font-weight: 900; font-size: 104px; line-height: 1;
  }
  .conclusion {
    left: 446px; top: 1922px; color: var(--signal-red);
    font-family: "Montserrat", sans-serif; font-weight: 700; font-size: 32px;
    letter-spacing: 2px; line-height: 49.5px;
  }
  .conclusion ol { list-style: none; }
</style>
</head>
<body>
  <div class="abs top-band"></div>
  <header class="abs title-box">
    <div class="inner">
      <h1>PERCENT OF AMERICANS TO FEEL FATIGUE<br>AND OVERLOADED BY THE COVID MESSAGES</h1>
      <p class="source">“Based on a survey of 400 U.S. adults conducted March 20-24th, 2020.”</p>
    </div>
  </header>

  <!-- Message Fatigue -->
  <div class="abs band blue" style="top:298px"></div>
  <div class="abs tab blue" style="left:444px;top:250px;width:311px"><span>Message Fatigue</span></div>
  <div class="abs art fatigue" style="top:306px" role="img" aria-label="Illustration of a stressed man holding his temples, worn out by messages"></div>
  <svg class="abs ring" style="left:469px;top:315px" viewBox="0 0 262 262">
    <circle cx="131" cy="131" r="108" fill="none" stroke="var(--ring-white)" stroke-width="46"/>
    <circle cx="131" cy="131" r="108" fill="none" stroke="var(--signal-red)" stroke-width="46" stroke-dasharray="373.2 678.6" transform="rotate(-90 131 131)"/>
    <circle cx="131" cy="131" r="85" fill="var(--navy)"/>
  </svg>
  <div class="abs ring-label" style="left:469px;top:402px">55%</div>
  <p class="abs stat-text" style="top:392px">feel exhausted<br>by all the messages</p>

  <!-- Information Overload -->
  <div class="abs band green" style="top:643px"></div>
  <div class="abs tab green" style="left:393px;top:597px;width:413px"><span>Information Overload</span></div>
  <div class="abs art overload" style="top:653px" role="img" aria-label="Illustration of a stressed man surrounded by a TV, laptop, phone and envelopes with notification counts"></div>
  <svg class="abs ring" style="left:469px;top:663px" viewBox="0 0 262 262">
    <circle cx="131" cy="131" r="108" fill="none" stroke="var(--ring-white)" stroke-width="46"/>
    <circle cx="131" cy="131" r="108" fill="none" stroke="var(--signal-red)" stroke-width="46" stroke-dasharray="373.2 678.6" transform="rotate(-90 131 131)"/>
    <circle cx="131" cy="131" r="85" fill="var(--forest)"/>
  </svg>
  <div class="abs ring-label" style="left:469px;top:750px">55%</div>
  <p class="abs stat-text" style="top:717px">feel overloaded by<br>the amount of<br>information</p>

  <!-- Perceived Message Repetition -->
  <div class="abs band blue" style="top:983px"></div>
  <div class="abs tab blue" style="left:334px;top:944px;width:531px"><span>Perceived Message Repetition</span></div>
  <div class="abs art repetition" style="top:992px" role="img" aria-label="Illustration of a phone and laptop inbox filled with repeated COVID-19 messages"></div>
  <svg class="abs ring" style="left:469px;top:1006px" viewBox="0 0 262 262">
    <circle cx="131" cy="131" r="108" fill="none" stroke="var(--ring-white)" stroke-width="46"/>
    <circle cx="131" cy="131" r="108" fill="none" stroke="var(--signal-red)" stroke-width="46" stroke-dasharray="346.1 678.6" transform="rotate(-90 131 131)"/>
    <circle cx="131" cy="131" r="85" fill="var(--navy)"/>
  </svg>
  <div class="abs ring-label" style="left:469px;top:1093px">51%</div>
  <p class="abs stat-text" style="top:1060px">feel that the<br>messages are<br>repetitive</p>

  <!-- Perceived Message Exaggeration -->
  <div class="abs band green" style="top:1320px"></div>
  <div class="abs tab green" style="left:305px;top:1281px;width:590px"><span>Perceived Message Exaggeration</span></div>
  <div class="abs art exaggeration" style="top:1330px" role="img" aria-label="Illustration of a masked man with virus particles, toilet paper and hand sanitizer"></div>
  <svg class="abs ring" style="left:469px;top:1342px" viewBox="0 0 262 262">
    <circle cx="131" cy="131" r="108" fill="none" stroke="var(--ring-white)" stroke-width="46"/>
    <circle cx="131" cy="131" r="108" fill="none" stroke="var(--signal-red)" stroke-width="46" stroke-dasharray="318.9 678.6" transform="rotate(-90 131 131)"/>
    <circle cx="131" cy="131" r="85" fill="var(--forest)"/>
  </svg>
  <div class="abs ring-label" style="left:469px;top:1429px">47%</div>
  <p class="abs stat-text" style="top:1396px">feel like messages<br>exaggerate how bad<br>it is</p>

  <!-- Conclusion -->
  <div class="abs bottom-band"></div>
  <div class="abs question-box">
    <div class="inner">WHAT DOES ALL THE ABOVE DATA<br>CONCLUDE?</div>
  </div>

  <svg class="abs summary-ring" viewBox="0 0 386 386">
    <circle cx="193" cy="193" r="159" fill="none" stroke="#f7f7f7" stroke-width="68"/>
    <circle cx="193" cy="193" r="159" fill="none" stroke="var(--signal-red)" stroke-width="68" stroke-dasharray="519.5 999" transform="rotate(-90 193 193)"/>
    <circle cx="193" cy="193" r="125" fill="var(--canvas)"/>
  </svg>
  <div class="abs summary-label">52%</div>

  <div class="abs conclusion">
    <p>It concluded that , almost half of U.S.<br>adults show sign of</p>
    <ol>
      <li>1. Message Fatigue</li>
      <li>2. Information Overload</li>
      <li>3. Perceived Message Repetition &amp;</li>
      <li>4. Perceived Message Exaggeration</li>
    </ol>
  </div>
</body>
</html>
```